3 x DIN A4 Flyer, Vorder- und Rückseite
Zielgruppe
Handwerksunternehmen
Aufgabenstellung
Wir benötigen 3 Werbeflyer die in Zeitschriften beigelegt werden. Jeweils DIN A4, Vorderseite beschreibt das Produkt, Rückseite kann zur Bestellung mittels Faxantwort benutzt werden. Profibilder und Text wird vollständig geliefert.

```html
<!DOCTYPE html>
<html lang="de">
<head>
<meta charset="utf-8">
<title>Prospektbox für die Baustelle</title>
<link href="https://fonts.googleapis.com/css2?family=Exo+2:ital,wght@0,400;0,600;0,700;0,800;1,900&display=swap" rel="stylesheet">
<style>
  :root {
    --blue: #1fa3dc;
    --blue-dark: #1789c0;
    --grey-text: #4d4d4d;
    --grey-light: #6a6a6a;
    --stage: #a3a3a3;
    --paper: #ffffff;
    --yellow: #ffe400;
    --placeholder: #e4eef3;
  }
  * { box-sizing: border-box; margin: 0; padding: 0; }
  html, body { width: 933px; height: 1200px; overflow: hidden; }
  body {
    background: var(--stage);
    font-family: "Exo 2", sans-serif;
    color: var(--grey-text);
    position: relative;
  }
  .flyer {
    position: absolute;
    left: 66px; top: 34px;
    width: 800px; height: 1131px;
    background: var(--paper);
    box-shadow: 0 4px 18px rgba(0,0,0,.35);
    overflow: hidden;
  }
  .edge-strip {
    position: absolute; left: 0; top: 63px;
    width: 33px; height: 79px;
    background: var(--blue);
  }
  .headline { position: absolute; left: 69px; top: 60px; width: 360px; }
  .headline h1 {
    font-size: 50px; font-weight: 800; color: var(--blue);
    line-height: 1; white-space: nowrap;
    transform: scaleX(0.8); transform-origin: left center;
  }
  .headline h2 {
    font-size: 26px; font-weight: 700; color: var(--grey-text);
    line-height: 1; margin-top: 2px; white-space: nowrap;
  }
  .format-tab {
    position: absolute; left: 448px; top: 59px;
    width: 352px; height: 83px;
    background: var(--blue);
    border-radius: 10px 0 0 10px;
    color: #fff; font-size: 26px; font-weight: 600;
    padding: 27px 0 0 38px;
  }
  .intro { position: absolute; left: 69px; top: 186px; width: 420px; }
  .intro .lead { font-size: 23px; font-weight: 700; line-height: 1; }
  .intro .lead-sub { font-size: 19px; font-weight: 600; line-height: 1.15; }
  .intro .highlight {
    font-size: 25px; font-weight: 700; color: var(--blue);
    line-height: 1.02; margin-top: 24px; white-space: nowrap;
  }
  .intro .note { font-size: 14px; line-height: 1.35; margin-top: 30px; color: var(--grey-light); }
  .intro .option { font-size: 25px; font-weight: 700; line-height: 1.05; margin-top: 20px; }
  .product-photo {
    position: absolute; border-radius: 6px;
    background: linear-gradient(160deg, #f4f8fa 0%, var(--placeholder) 60%, #cfdde5 100%);
  }
  .product-photo.top { left: 468px; top: 217px; width: 190px; height: 280px; }
  .product-photo.bottom {
    left: 55px; top: 632px; width: 200px; height: 250px;
    background: linear-gradient(170deg, #eef4f7 0%, #b9dcee 55%, #3aa9dc 100%);
  }
  .badge { position: absolute; left: 508px; top: 346px; width: 100px; height: 100px; }
  .benefit { position: absolute; left: 290px; width: 470px; display: flex; gap: 22px; }
  .benefit svg { flex: none; margin-top: 22px; }
  .benefit p { font-size: 19px; line-height: 1.3; color: var(--grey-text); }
  .benefit.one { top: 645px; }
  .benefit.two { top: 763px; }
  .sender { position: absolute; left: 69px; top: 925px; width: 280px; font-style: normal; }
  .sender .name { font-size: 16px; font-weight: 700; line-height: 1.35; }
  .sender .address { font-size: 15px; line-height: 1.4; margin-top: 20px; color: var(--grey-light); }
  .sender .web { font-size: 19px; font-weight: 700; margin-top: 24px; }
  .price-box {
    position: absolute; left: 355px; top: 940px;
    width: 445px; height: 191px;
    background: var(--blue);
    border-radius: 12px 0 0 0;
  }
  .price {
    position: absolute; left: 376px; top: 900px;
    font-size: 76px; font-weight: 900; font-style: italic;
    color: var(--yellow); line-height: 1;
    text-shadow: 2px 3px 0 var(--blue-dark);
  }
  .price small { font-size: 30px; margin-left: 8px; }
  .price-terms {
    position: absolute; left: 374px; top: 1030px; width: 410px;
    font-size: 14px; line-height: 1.3; color: #1d2a33;
  }
</style>
</head>
<body>
  <main class="flyer">
    <div class="edge-strip"></div>

    <header class="headline">
      <h1>PROSPEKTBOX</h1>
      <h2>FÜR DIE BAUSTELLE</h2>
    </header>
    <div class="format-tab">DIN A4 Hochformat</div>

    <section class="intro">
      <p class="lead">Mit einem Klick</p>
      <p class="lead-sub">erwerben Sie zu einem absoluten<br>Sonderpreis</p>
      <p class="highlight">die neue und wetterfeste<br>DIN A4 Hochformat Prospektbo<br>mit Deckel zur Wandmontage</p>
      <p class="note">(Montage-Schrauben sind im<br>Lieferumfang NICHT enthalten)</p>
      <p class="option">oder Pfostenmontage<br>mittels Kunststoffbinder</p>
      <p class="note">(im Lieferumfang enthalten)</p>
      <p class="option">und Hohlkehle an der Rückseite<br>des Displays.</p>
    </section>

    <div class="product-photo top" role="img" aria-label="Produktfoto: transparente Prospektbox aus Acryl mit Klappdeckel"></div>

    <svg class="badge" viewBox="0 0 120 120" aria-label="Neu">
      <polygon fill="#1fa3dc" points="60,2 69,22 88,9 89,32 112,30 102,51 120,62 101,74 110,95 87,95 84,118 65,104 50,120 43,98 20,106 24,83 2,74 18,59 4,40 27,37 25,14 46,24"/>
      <text x="60" y="70" text-anchor="middle" transform="rotate(-15 60 62)" font-family="Exo 2, sans-serif" font-weight="800" font-size="28" fill="#fff">NEU</text>
    </svg>

    <div class="product-photo bottom" role="img" aria-label="Produktfoto: Prospektbox mit eingelegtem blauen Werbeflyer „Ihre Werbung hier“"></div>

    <div class="benefit one">
      <svg width="49" height="40" viewBox="0 0 49 40" aria-hidden="true"><path d="M2 22 L10 16 L19 28 L44 2 L48 6 L19 38 Z" fill="#1fa3dc"/></svg>
      <p>Die ideale Aussenbox für die Präsentation Ihrer Flyer, Prospekte und Informationen in allen Aussenbereichen.</p>
    </div>
    <div class="benefit two">
      <svg width="49" height="40" viewBox="0 0 49 40" aria-hidden="true"><path d="M2 22 L10 16 L19 28 L44 2 L48 6 L19 38 Z" fill="#1fa3dc"/></svg>
      <p>Ihre Werbemittel werden durch einen Deckel vor Nässe geschützt. Bohrungen für die Wandmontage vorhanden.</p>
    </div>

    <address class="sender">
      <p class="name">Kooperationsverband<br>Leicht- und<br>Trockenbau mbH</p>
      <p class="address">Lindenhofer Straße 24<br>80999 Musterstadt</p>
      <p class="web">www.kltr.de</p>
    </address>

    <div class="price-box"></div>
    <p class="price">26,-<small>netto</small></p>
    <p class="price-terms">Alle angegebenen Preise verstehen sich in Euro zzgl. der gesetzlichen geltenden Mehrwertsteuer von derzeit 19%. Die Lieferung erfolgt ca.10 Tage nach Bestelleingang. Porto/Verpackung 8,90 Euro</p>
  </main>
</body>
</html>
```